Soap box for artisan soaps, eco-look, high design

We need a soap box for our lovely artisan soaps. The box size is: 9 cm height x 6,5 cm width x 2,8 cm depth. It would be nice when there is a small window in the box so you can see the soap.

See attachment for an example soap box (upside down). Please use the same elements such as texts and industrie logos. The idea is that we have a generic design that we can custom-made for different soaps. We have 15 different soaps in total at the moment.

Target Market(s)

Middle to high income

Font styles to use
Decorative
Script

Requirements
Must have
• Dutch text:
• Etherische oliën
• Handgemaakt
• Natuurlijke ingrediënten

```html
<!DOCTYPE html>
<html lang="nl">
<head>
<meta charset="utf-8">
<title>Velmora – Etherische Zeep</title>
<link rel="stylesheet" href="https://fonts.googleapis.com/css2?family=Playfair+Display:wght@700&family=Parisienne&family=Arimo:wght@400&display=swap">
<style>
  :root {
    --page: #ffffff;
    --kraft: #b4936f;
    --kraft-side: #a1815f;
    --kraft-lower: #a9885f;
    --navy: #1d3a56;
    --ink: #2a2118;
    --white: #fbf7f1;
    --lemon: #d8b238;
    --lavender: #c98ea8;
    --orange: #dba13e;
  }
  html, body {
    margin: 0;
    width: 1200px;
    height: 946px;
    overflow: hidden;
    background: var(--page);
  }
  .range {
    position: relative;
    width: 1200px;
    height: 946px;
    display: flex;
    justify-content: center;
    align-items: center;
    gap: 40px;
  }
  .box {
    display: flex;
    height: 400px;
    box-shadow: 0 18px 30px -18px rgba(0,0,0,0.25);
  }
  .box__side {
    width: 48px;
    height: 100%;
    background: var(--kraft-side);
    display: flex;
    justify-content: center;
    padding-top: 10px;
    box-sizing: border-box;
  }
  .ingredients {
    writing-mode: vertical-rl;
    transform: rotate(180deg);
    font-family: "Arimo", sans-serif;
    font-size: 6.4px;
    line-height: 1.3;
    color: var(--ink);
    height: 220px;
    margin: 0;
    text-align: justify;
  }
  .ingredients b { font-weight: 700; }
  .box__front {
    position: relative;
    width: 255px;
    height: 100%;
    background: var(--kraft);
    overflow: hidden;
    text-align: center;
  }
  .brand {
    position: absolute;
    top: 22px;
    left: 0; right: 0;
    margin: 0;
    font-family: "Playfair Display", serif;
    font-weight: 700;
    font-size: 34px;
    color: var(--navy);
    letter-spacing: 0.5px;
  }
  .variant {
    position: absolute;
    top: 72px;
    left: 0; right: 0;
    margin: 0;
    font-family: "Parisienne", cursive;
    font-size: 27px;
    color: var(--ink);
    font-weight: 400;
  }
  .category {
    position: absolute;
    top: 116px;
    left: 0; right: 0;
    margin: 0;
    font-family: "Arimo", sans-serif;
    font-size: 15px;
    color: var(--ink);
    letter-spacing: 0.2px;
  }
  .lower {
    position: absolute;
    left: 0; right: 0;
    top: 218px;
    bottom: 0;
    background: var(--kraft-lower);
  }
  .stripe {
    position: absolute;
    left: 0; right: 0;
    top: 212px;
    height: 6px;
  }
  .box--lemon .stripe { background: var(--lemon); }
  .box--lavender .stripe { background: var(--lavender); }
  .box--orange .stripe { background: var(--orange); }
  .window {
    position: absolute;
    left: 50%;
    top: 146px;
    width: 128px;
    height: 136px;
    margin-left: -64px;
    border-radius: 50%;
    box-shadow: inset 0 0 8px rgba(0,0,0,0.35);
  }
  .box--lemon .window { background: linear-gradient(90deg, #c98a2e, #dca048 45%, #b98a52 80%, #a88a75); }
  .box--lavender .window { background: linear-gradient(110deg, #bcaed8, #e3dcef 40%, #8d6fd0 65%, #cfc4e6); }
  .box--orange .window { background: linear-gradient(120deg, #f2d6bd, #f0b794 45%, #ec9a72 60%, #f3d1b7); }
  .claims {
    position: absolute;
    left: 0; right: 0;
    top: 296px;
    margin: 0;
    padding: 0;
    list-style: none;
    font-family: "Arimo", sans-serif;
    font-size: 15px;
    line-height: 24px;
    color: var(--white);
  }
</style>
</head>
<body>
<main class="range">

  <article class="box box--lemon">
    <aside class="box__side">
      <p class="ingredients"><b>Ingredients:</b> Olijf olie pomace (Olea europaea), Kokosnoot olie (Cocos nucifera), Palm olie (Elaeis Guineensis Kernel Oil), Water (Aqua), Citroen Etherische Olie (Citrus limonum), maanzaad (Papaver somniferum), IJzer oxide geel (Iron Oxide). Natuurlijke bestanddelen van Etherische Olie – Citral, Citronellol, Geraniol, Limonene, Linalool.</p>
    </aside>
    <section class="box__front">
      <div class="lower" role="img" aria-label="Fijn stippenpatroon op kraftpapier"></div>
      <div class="stripe"></div>
      <h1 class="brand">Velmora</h1>
      <h2 class="variant">Lemon and Poppy</h2>
      <p class="category">ETHERISCHE ZEEP</p>
      <div class="window" role="img" aria-label="Venster met zicht op gele citroen-maanzaadzeep"></div>
      <ul class="claims">
        <li>Etherische oliën</li>
        <li>Handgemaakt</li>
        <li>Natuurlijke ingrediënten</li>
      </ul>
    </section>
  </article>

  <article class="box box--lavender">
    <aside class="box__side">
      <p class="ingredients"><b>Ingredients:</b> Olijf olie pomace (Olea europaea), Kokosnoot olie (Cocos nucifera), Palm olie (Elaeis Guineensis Kernel Oil), Water (Aqua), Citroen Etherische Olie (Citrus limonum), maanzaad (Papaver somniferum), IJzer oxide geel (Iron Oxide). Natuurlijke bestanddelen van Etherische Olie – Citral, Citronellol, Geraniol, Limonene, Linalool.</p>
    </aside>
    <section class="box__front">
      <div class="lower" role="img" aria-label="Fijn stippenpatroon op kraftpapier"></div>
      <div class="stripe"></div>
      <h1 class="brand">Velmora</h1>
      <h2 class="variant">Lavender</h2>
      <p class="category">ETHERISCHE ZEEP</p>
      <div class="window" role="img" aria-label="Venster met zicht op paars-witte lavendelzeep"></div>
      <ul class="claims">
        <li>Etherische oliën</li>
        <li>Handgemaakt</li>
        <li>Natuurlijke ingrediënten</li>
      </ul>
    </section>
  </article>

  <article class="box box--orange">
    <aside class="box__side">
      <p class="ingredients"><b>Ingredients:</b> Olijf olie pomace (Olea europaea), Kokosnoot olie (Cocos nucifera), Palm olie (Elaeis Guineensis Kernel Oil), Water (Aqua), Citroen Etherische Olie (Citrus limonum), maanzaad (Papaver somniferum), IJzer oxide geel (Iron Oxide). Natuurlijke bestanddelen van Etherische Olie – Citral, Citronellol, Geraniol, Limonene, Linalool.</p>
    </aside>
    <section class="box__front">
      <div class="lower" role="img" aria-label="Fijn stippenpatroon op kraftpapier"></div>
      <div class="stripe"></div>
      <h1 class="brand">Velmora</h1>
      <h2 class="variant">Orange Sweet</h2>
      <p class="category">ETHERISCHE ZEEP</p>
      <div class="window" role="img" aria-label="Venster met zicht op zachtoranje sinaasappelzeep"></div>
      <ul class="claims">
        <li>Etherische oliën</li>
        <li>Handgemaakt</li>
        <li>Natuurlijke ingrediënten</li>
      </ul>
    </section>
  </article>

</main>
</body>
</html>
```